Sunny Paths and joy Business card

I have a logo, but will like a business card design. Is for a travel agency in Mexico. We focus in family experiences.

I will liek some thing different and unique, from the traditional business card, something to get remmeber for.

Business card information:

Leandro T. Ocampo
leandro@sunnypathsjoy.example

Alameda 482, 3 piso
Col. Tlalpizco
Mexico, D.F. 07320

office: (55) 5000-0142
mobile: (55) 9000-0187

www.sunnypathsjoy.example
@sunnypjoy
blog: sunnypathsandjoy.blogsite.example
facebook: SunnyPathsAndJoy

```html
<!DOCTYPE html>
<html lang="en">
<head>
<meta charset="utf-8">
<title>Sunny Paths and joy — Business Card</title>
<link rel="stylesheet" href="https://fonts.googleapis.com/css2?family=Questrial&display=swap">
<style>
  :root {
    --page-bg: #e9edf0;
    --card-white: #ffffff;
    --brand-blue: #1f6ea8;
    --brand-blue-deep: #19639a;
    --brand-blue-light: #2f86c4;
    --name-blue: #2d7fbd;
    --link-blue: #2a86c8;
    --text-dark: #2b2f33;
    --map-tint: #3a8ccb;
  }
  * { box-sizing: border-box; margin: 0; padding: 0; }
  html, body {
    width: 1200px; height: 960px; overflow: hidden;
    background: var(--page-bg);
    font-family: "Questrial", "Century Gothic", sans-serif;
  }
  .sheet {
    width: 1200px; height: 960px;
    display: flex; flex-direction: column; align-items: center; justify-content: center;
    gap: 60px;
  }
  .card {
    width: 700px; height: 400px; position: relative; overflow: hidden;
    box-shadow: 0 6px 18px rgba(20, 40, 60, .18);
  }

  /* Back side */
  .card--back {
    background: linear-gradient(160deg, var(--brand-blue-light), var(--brand-blue) 60%, var(--brand-blue-deep));
  }
  .card--back .map-area {
    position: absolute; left: 40px; top: 50px; width: 620px; height: 300px;
    border-radius: 40px;
    background: radial-gradient(ellipse at center, rgba(80,160,220,.35), rgba(80,160,220,.08) 70%, transparent);
  }

  /* Front side */
  .card--front { background: var(--card-white); }
  .holder-name {
    position: absolute; left: 44px; top: 38px;
    font-size: 30px; color: var(--name-blue); font-weight: 400; letter-spacing: .5px;
  }
  .contact-list {
    position: absolute; left: 44px; top: 104px; list-style: none;
  }
  .contact-list li {
    display: flex; align-items: center; gap: 16px;
    font-size: 20px; line-height: 26px; color: var(--text-dark); letter-spacing: .4px;
  }
  .contact-list li.is-link { color: var(--link-blue); }
  .contact-list .icon { width: 14px; height: 14px; flex: none; }
  .contact-list .icon * { fill: var(--brand-blue); stroke: none; }
  .contact-list .icon .stroke { fill: none; stroke: var(--brand-blue); stroke-width: 1.6; }

  .brand-mark {
    position: absolute; right: 44px; top: 120px;
    display: flex; align-items: center; gap: 12px;
  }
  .brand-mark .dot {
    width: 26px; height: 26px; border-radius: 50%; background: var(--brand-blue);
  }
  .brand-mark .brand-name {
    font-size: 28px; color: var(--brand-blue); line-height: 1.1; width: 170px;
  }

  .address-band {
    position: absolute; left: 0; right: 0; bottom: 0; height: 56px;
    background: var(--brand-blue);
    color: var(--card-white);
    font-size: 19px; letter-spacing: .8px;
    display: flex; align-items: center; justify-content: center;
  }
</style>
</head>
<body>
<main class="sheet">

  <section class="card card--back" aria-label="Business card back">
    <div class="map-area" role="img" aria-label="Dotted world map pattern in lighter blue"></div>
  </section>

  <section class="card card--front" aria-label="Business card front">
    <h1 class="holder-name">Leandro T. Ocampo</h1>

    <ul class="contact-list">
      <li>
        <svg class="icon" viewBox="0 0 14 14" aria-hidden="true"><path d="M3 1 L5 1 L6 4 L4.5 5.2 Q6 8.2 8.8 9.5 L10 8 L13 9 L13 11 Q12 13 10 13 Q2 11 1 3 Q1 1 3 1 Z"/></svg>
        (55) 5000-0142
      </li>
      <li>
        <svg class="icon" viewBox="0 0 14 14" aria-hidden="true"><rect x="3.5" y="0.5" width="7" height="13" rx="1.5"/><rect x="5" y="2" width="4" height="8" fill="#fff"/></svg>
        (55) 9000-0187
      </li>
      <li>
        <svg class="icon" viewBox="0 0 14 14" aria-hidden="true"><rect x="0.5" y="2.5" width="13" height="9"/><path class="stroke" d="M1 3 L7 8 L13 3" style="stroke:#fff"/></svg>
        leandro@sunnypathsjoy.example
      </li>
      <li class="is-link">
        <svg class="icon" viewBox="0 0 14 14" aria-hidden="true"><circle class="stroke" cx="7" cy="7" r="6"/><path class="stroke" d="M1 7 H13 M7 1 Q3 7 7 13 M7 1 Q11 7 7 13"/></svg>
        www.sunnypathsjoy.example
      </li>
      <li>
        <svg class="icon" viewBox="0 0 14 14" aria-hidden="true"><circle cx="7" cy="7" r="6"/></svg>
        sunnypathsandjoy.blogsite.example
      </li>
      <li>
        <svg class="icon" viewBox="0 0 14 14" aria-hidden="true"><rect x="1" y="1" width="12" height="12" rx="1.5"/></svg>
        SunnyPathsAndJoy
      </li>
      <li>
        <svg class="icon" viewBox="0 0 14 14" aria-hidden="true"><rect x="1" y="1" width="12" height="12" rx="1.5"/></svg>
        @sunnypjoy
      </li>
    </ul>

    <div class="brand-mark">
      <span class="dot" aria-hidden="true"></span>
      <span class="brand-name">Sunny Paths and joy</span>
    </div>

    <footer class="address-band">Alameda 482, 3 piso Col. Tlalpizco Mexico, D.F. 07320</footer>
  </section>

</main>
</body>
</html>
```